Packaging box design (uLumo style)

To create a striking but minimalist box for a new tool handle. The top sleeve external box dimensions are L230xW85xH65mm. We will need the logo (plia by KVR), you can use any of our rendered drawings if you feel it would look good. Information to be included; Ergonomic Adjustable Handle / 12 position lock system / Quick release shaft / Weight and space saving / Comfort grip / Ability to convert existing toolsFor purchase and converting options please visit (USA) www.brasolmark.com or (Europe) www.kvrtools.com.

Target Market(s)

Automotive professionals

Font styles to use
Sans Serif

Colors
fbed22
333333
5c5c5c
9d9d9d

Requirements
Must have
• Logo - plia by KVR (attached)

```html
<!DOCTYPE html>
<html lang="en">
<head>
<meta charset="UTF-8">
<title>plia series by KVR – Sleeve Artwork</title>
<link rel="stylesheet" href="https://fonts.googleapis.com/css2?family=Lato:wght@300;400;700;900&display=swap">
<style>
  :root {
    --brand-yellow: #fbed22;
    --ink-dark: #333333;
    --ink-mid: #5c5c5c;
    --ink-light: #9d9d9d;
    --panel-black: #2b2b2b;
    --panel-white: #f4f5f7;
    --stage: #dcdde0;
    --text-on-dark: #e6e6e6;
    --gold-light: #e8dca6;
    --gold-mid: #cdb044;
    --gold-deep: #a58a2c;
  }
  * { box-sizing: border-box; margin: 0; padding: 0; }
  html, body {
    width: 1200px; height: 900px; overflow: hidden;
    background: var(--stage);
    font-family: "Lato", Arial, sans-serif;
  }
  .sleeve-layout { position: relative; width: 1200px; height: 900px; }

  .panel { position: absolute; overflow: hidden; }

  /* Top face */
  .panel-top {
    left: 60px; top: 150px; width: 760px; height: 281px;
    background: var(--panel-white);
  }
  .panel-top .dark-band { position: absolute; inset: 0; width: 100%; height: 100%; }
  .panel-top .product-render {
    position: absolute; left: 28px; top: 78px; width: 420px; height: 150px;
    border-radius: 75px 40px 40px 75px;
    background: linear-gradient(180deg, var(--gold-light) 0%, var(--gold-mid) 55%, var(--gold-deep) 100%);
  }
  .brand-mark {
    font-family: "Lato", Arial, sans-serif;
    font-weight: 900; line-height: 0.9;
    display: flex; flex-direction: column; align-items: flex-start;
  }
  .brand-mark .brand-name { font-size: 64px; letter-spacing: -1px; }
  .brand-mark .brand-sub { font-size: 20px; margin-left: 28px; }
  .panel-top .brand-mark {
    position: absolute; right: 40px; top: 20px; color: var(--ink-dark);
  }
  .feature-list {
    position: absolute; right: 34px; top: 128px; width: 250px;
    color: var(--text-on-dark); list-style: none;
  }
  .feature-list .feature-title {
    font-size: 15px; font-weight: 400; padding-bottom: 6px;
    border-bottom: 1px solid var(--ink-mid); margin-bottom: 6px;
  }
  .feature-list li { font-size: 12px; line-height: 1.5; font-weight: 300; }
  .feature-list li.strong { font-weight: 700; font-size: 13px; }

  /* Long side face */
  .panel-side {
    left: 60px; top: 431px; width: 760px; height: 215px;
    background: var(--panel-black);
    border-top: 1px solid #444;
  }
  .panel-side .brand-mark {
    position: absolute; left: 34px; top: 62px; color: var(--brand-yellow);
  }
  .panel-side .handle-drawing {
    position: absolute; left: 260px; top: 44px; width: 470px; height: 130px;
    border-radius: 20px; background: #3a3a2a;
  }
  .panel-side .thumb-notch {
    position: absolute; left: 50%; top: -1px; width: 70px; height: 22px;
    margin-left: -35px; background: var(--stage);
    border-radius: 0 0 35px 35px;
  }

  /* End face */
  .panel-end {
    left: 840px; top: 431px; width: 281px; height: 215px;
    background: var(--panel-black);
    display: flex; align-items: center; justify-content: center;
  }
  .panel-end .brand-mark { color: var(--brand-yellow); }
</style>
</head>
<body>
<main class="sleeve-layout">

  <section class="panel panel-top">
    <svg class="dark-band" viewBox="0 0 760 281" preserveAspectRatio="none" aria-hidden="true">
      <path d="M0 281 L0 250 C 200 250 320 150 470 120 C 600 95 700 100 760 100 L760 281 Z" fill="#2b2b2b"/>
    </svg>
    <div class="product-render" role="img" aria-label="Rendered gold ergonomic tool handle lying across the lid"></div>
    <div class="brand-mark">
      <span class="brand-name">plia</span>
      <span class="brand-sub">series by KVR</span>
    </div>
    <ul class="feature-list">
      <li class="feature-title">Ergonomic Adjustable Handle</li>
      <li>- 12 position lock system</li>
      <li class="strong">- Quick release shaft</li>
      <li>- Weight and space saving</li>
      <li class="strong">- Comfort grip</li>
      <li>- Ability to convert existing tools</li>
    </ul>
  </section>

  <section class="panel panel-side">
    <div class="thumb-notch"></div>
    <div class="brand-mark">
      <span class="brand-name">plia</span>
      <span class="brand-sub">series by KVR</span>
    </div>
    <div class="handle-drawing" role="img" aria-label="Yellow line drawing of the handle in side view"></div>
  </section>

  <section class="panel panel-end">
    <div class="brand-mark">
      <span class="brand-name">plia</span>
      <span class="brand-sub">series by KVR</span>
    </div>
  </section>

</main>
</body>
</html>
```